Energieberatung sucht Corporate Design
Zielgruppe
Ich führe Energieberatungen für Immobilieneigentümer durch, erstelle Sanierungsvorschläge sowie Förderanträge. Für Verkäufer und Vermieter fertige ich Energieausweise an, um die energetisch Qualität des Gebäudes darzustellen.
Energieberatung soll für die Kunden ein Wegweiser für modernes, klimaneutrales und kostengünstiges Wohnen sein.
Meine Zielgruppe sind Immobilieneigentümer, Verkäufer und Vermieter von Immobilien sowie Käufer von Immobilien.
Aufgabenstellung
Ich suche ein hochwertiges Design, welches modern und zeitlos ist, aber auch die energetische Komponente berücksichtigt. Mit dem Design soll das verstaubte Image der Energieberatung abgelegt werden. Die Kunden sollen damit zukunftsorientiertes, modernes Wohnen, Wohnqualität und Kostenersparnis verbinden.

```html
<!DOCTYPE html>
<html lang="de">
<head>
<meta charset="utf-8">
<title>Energieberatung Lena Varholt – Corporate Design</title>
<link href="https://fonts.googleapis.com/css2?family=Arimo:wght@400;600&display=swap" rel="stylesheet">
<style>
  :root{
    --teal:#10788f;
    --grey-text:#5a5a5a;
    --dark:#333;
    --stage:#a3aab3;
    --paper:#ffffff;
    --paper-warm:#f1f0ed;
    --rule:#c9ccd0;
    --black:#1b1b1b;
  }
  *{box-sizing:border-box;margin:0;padding:0}
  html,body{width:997px;height:1200px;overflow:hidden}
  body{background:var(--stage);font-family:'Arimo',Arial,sans-serif;color:var(--dark);position:relative}
  .sheet{position:absolute;background:var(--paper);box-shadow:0 3px 10px rgba(0,0,0,.25)}

  .wordmark{display:flex;align-items:center;gap:8px;color:var(--teal);font-weight:600;letter-spacing:.08em;line-height:1.15;text-transform:uppercase}
  .wordmark .mark-square{flex:none;background:var(--teal)}
  .wordmark--black{color:var(--black)}
  .wordmark--black .mark-square{background:var(--black)}

  .logo-card{left:52px;top:28px;width:488px;height:263px;display:flex;align-items:center;justify-content:center;box-shadow:none}
  .logo-card .wordmark{font-size:16px}
  .logo-card .mark-square{width:44px;height:44px}

  .paper-card{left:562px;top:28px;width:375px;height:265px;background:var(--paper-warm);display:flex;align-items:center;justify-content:center;box-shadow:none}
  .paper-card .wordmark{font-size:13px}
  .paper-card .mark-square{width:36px;height:36px}

  .small .wordmark{font-size:8.5px;gap:6px}
  .small .mark-square{width:22px;height:22px}

  .card-front{left:53px;top:340px;width:235px;height:152px}
  .card-front .wordmark{position:absolute;left:17px;top:18px}
  .card-front .role{position:absolute;left:17px;top:74px;font-size:7.5px}
  .accent{color:var(--teal)}
  .card-front .address{position:absolute;left:17px;top:103px;font-size:6.5px;line-height:1.5}
  .contacts{list-style:none;font-size:6.5px;line-height:1.5}
  .contacts li{display:flex;align-items:center;gap:5px}
  .contacts svg{width:7px;height:7px;flex:none}
  .card-front .contacts{position:absolute;left:130px;top:103px}
  .card-front .base-bar{position:absolute;left:16px;bottom:0;width:203px;height:7px;background:var(--teal)}

  .card-back{left:53px;top:508px;width:235px;height:152px;background:var(--teal);display:flex;flex-direction:column;align-items:center;justify-content:center;gap:12px}
  .card-back .mark-square{width:44px;height:44px;background:#e9c21a}
  .card-back .url{color:#f1c40f;font-size:9px;letter-spacing:.05em}

  .letterhead{left:361px;top:339px;width:580px;height:820px}
  .letterhead .wordmark{position:absolute;left:58px;top:42px;font-size:9px}
  .letterhead .mark-square{width:28px;height:28px}
  .letterhead .sender{position:absolute;left:60px;top:125px;font-size:6px;color:var(--grey-text)}
  .letterhead .fold-mark{position:absolute;left:0;top:242px;width:20px;height:1px;background:var(--rule)}
  .letterhead .footer{position:absolute;left:60px;top:772px;display:flex;font-size:6.3px;line-height:1.65;color:var(--grey-text)}
  .footer .col{padding:0 7px;border-left:1px solid var(--teal);height:36px}
  .footer .col:first-child{padding-left:0;border-left:none}
  .footer .col h4{font-weight:400;color:var(--teal);font-size:6.3px}
  .footer .contacts{font-size:6.3px;line-height:1.45}
  .letterhead .base-bar{position:absolute;left:59px;bottom:0;width:478px;height:10px;background:var(--teal)}

  .envelope{left:51px;top:693px;width:501px;height:238px;border:1px solid #8d9299}
  .envelope .wordmark{position:absolute;left:28px;top:28px;font-size:8.5px}
  .envelope .mark-square{width:26px;height:26px}

  .mono-logo{position:absolute;left:94px;top:998px}
  .mono-logo .wordmark{font-size:8.5px}
  .mono-logo .mark-square{width:28px;height:28px}
</style>
</head>
<body>
<svg width="0" height="0" style="position:absolute">
  <defs>
    <symbol id="i-phone" viewBox="0 0 10 10"><path d="M2 1l2 0 1 2.5-1.2 1a5 5 0 0 0 2.7 2.7l1-1.2L10 7v2h-1A8 8 0 0 1 1 2V1z" fill="currentColor"/></symbol>
    <symbol id="i-fax" viewBox="0 0 10 10"><rect x="3" y="1" width="4" height="3" fill="none" stroke="currentColor"/><rect x="1" y="4" width="8" height="4" fill="none" stroke="currentColor"/><rect x="3" y="7" width="4" height="2" fill="currentColor"/></symbol>
    <symbol id="i-mail" viewBox="0 0 10 10"><rect x="1" y="2.5" width="8" height="5.5" fill="currentColor"/><path d="M1 2.5l4 3 4-3" fill="none" stroke="#fff" stroke-width=".8"/></symbol>
    <symbol id="i-web" viewBox="0 0 10 10"><circle cx="5" cy="5" r="4" fill="none" stroke="currentColor"/><ellipse cx="5" cy="5" rx="1.8" ry="4" fill="none" stroke="currentColor" stroke-width=".7"/><path d="M1 5h8" stroke="currentColor" stroke-width=".7"/></symbol>
  </defs>
</svg>

<section class="sheet logo-card">
  <div class="wordmark"><span class="mark-square"></span><span>Energieberatung<br>Lena Varholt</span></div>
</section>

<section class="sheet paper-card">
  <div class="wordmark"><span class="mark-square"></span><span>Energieberatung<br>Lena Varholt</span></div>
</section>

<section class="sheet card-front small">
  <div class="wordmark"><span class="mark-square"></span><span>Energieberatung<br>Lena Varholt</span></div>
  <p class="role"><span class="accent">Lena Varholt</span> - Geschäftsleitung</p>
  <p class="address">Musterstraße 126<br>00000 Musterstadt</p>
  <ul class="contacts">
    <li><svg class="accent"><use href="#i-phone"/></svg>+49 1234-56789-0</li>
    <li><svg class="accent"><use href="#i-fax"/></svg>+49 1234-56789-1</li>
    <li><svg class="accent"><use href="#i-mail"/></svg>info@varholt-beratung.de</li>
    <li><svg class="accent"><use href="#i-web"/></svg>www.varholt-beratung.de</li>
  </ul>
  <div class="base-bar"></div>
</section>

<section class="sheet card-back">
  <span class="mark-square"></span>
  <p class="url">www.varholt-beratung.de</p>
</section>

<section class="sheet letterhead">
  <div class="wordmark"><span class="mark-square"></span><span>Energieberatung<br>Lena Varholt</span></div>
  <p class="sender"><span class="accent">Energieberatung Lena Varholt</span> - Postfach 0000 - 00000 Musterstadt</p>
  <div class="fold-mark"></div>
  <div class="footer">
    <div class="col"><h4>Energieberatung Lena Varholt</h4>Musterstraße 126<br>00000 Musterstadt</div>
    <div class="col"><h4>Geschäftsleitung</h4>Lena Varholt</div>
    <div class="col">
      <ul class="contacts">
        <li><svg class="accent"><use href="#i-phone"/></svg>+49 1234-56789-0</li>
        <li><svg class="accent"><use href="#i-fax"/></svg>+49 1234-56789-1</li>
        <li><svg class="accent"><use href="#i-web"/></svg>www.varholt-beratung.de</li>
      </ul>
    </div>
    <div class="col"><h4>Amtsgericht Stadt</h4>ABC 0000XX<br>UST-ID DE 000XX</div>
    <div class="col"><h4>Bankverbindung ABC</h4>IBAN DE12 3456 7890 1234 5678<br>BIC ABCDEF12345</div>
  </div>
  <div class="base-bar"></div>
</section>

<section class="sheet envelope">
  <div class="wordmark"><span class="mark-square"></span><span>Energieberatung<br>Lena Varholt</span></div>
</section>

<div class="mono-logo">
  <div class="wordmark wordmark--black"><span class="mark-square"></span><span>Energieberatung<br>Lena Varholt</span></div>
</div>
</body>
</html>
```